Creative Out of the Box Post Up Banner Needed

I am looking for a great design for my banner. The design will be printed on a retractable vertical banner. Size 80 inches X 32 inches.

It will be displayed at my seminar and industry trade shows.

It needs to position me as a celebrity expert to grab people's attention. It shouldn't look boring.

Imagine a banner for a celebrity or a rock star.

It should look high-end and elegant.

The banner should include the entire body from head to toe, that makes it life-size when I print the banner.

Target Market(s)

salon and spa owners

Industry/Entity Type

Industry

Requirements
Must have
• My photo and a small book cover image.

You can download the images from:
http://www.glowtradecoach.com/images/bannerphoto.jpg
http://www.glowtradecoach.com/images/bookcover.jpg

Text that on the banner.

"Successful, rich, happy owners aren't smarter. They just play by a different set of rules."

Ivo Venn
#1 Business Expert In The Salon & Spa Industry
Millionaire Salon Owner
Best-Selling Author of Quiet Habits Of Parlor Keepers And A Ladder Out Of Debt
Nice to have
• Designs that I like.
http://www.artpitchhub.com/design/69852/poster-design-other-by-lumenpixo
http://mint-lantern.co.kr/pds/board/201108/poster.jpg
http://herbookedchairs.com/wp-content/uploads/2009/11/P10101561.jpg

```html
<!DOCTYPE html>
<html lang="en">
<head>
<meta charset="utf-8">
<title>Ivo Venn – Salon Business Expert Banner</title>
<link href="https://fonts.googleapis.com/css2?family=Arimo:wght@400;700&display=swap" rel="stylesheet">
<style>
  :root {
    --pink-deep: #e5306f;
    --pink-soft: #f6c3d5;
    --pink-pale: #fde9f0;
    --ink: #3b3b3b;
    --suit: #2a2a2e;
    --skin-tone: #c9a08a;
    --book-green: #3f7a3a;
    --book-cream: #f2f1e6;
  }
  * { margin: 0; padding: 0; box-sizing: border-box; }
  html, body { width: 1200px; height: 3075px; overflow: hidden; background: #ffffff; }
  .banner {
    position: relative;
    width: 1200px;
    height: 3075px;
    overflow: hidden;
    font-family: "Arimo", Arial, sans-serif;
  }
  .heart-backdrop {
    position: absolute;
    inset: 0;
    background:
      radial-gradient(ellipse at 30% 20%, var(--pink-pale) 0%, transparent 45%),
      radial-gradient(ellipse at 75% 60%, var(--pink-pale) 0%, transparent 40%),
      linear-gradient(180deg, var(--pink-soft) 0%, #f9d3e0 55%, var(--pink-soft) 100%);
  }
  .quote {
    position: absolute;
    left: 52px;
    top: 62px;
    width: 560px;
    color: var(--pink-deep);
    font-size: 90px;
    line-height: 101px;
    font-weight: 400;
    letter-spacing: -1px;
    white-space: nowrap;
  }
  .portrait {
    position: absolute;
    left: 650px;
    top: 112px;
    width: 320px;
    height: 2478px;
    border-radius: 110px 110px 40px 40px;
    background: linear-gradient(180deg, var(--skin-tone) 0%, var(--suit) 9%, var(--suit) 92%, #1a1a1c 100%);
  }
  .portrait-reflection {
    position: absolute;
    left: 670px;
    top: 2590px;
    width: 280px;
    height: 110px;
    background: linear-gradient(180deg, rgba(42,42,46,0.22) 0%, rgba(42,42,46,0) 100%);
  }
  .book-cover {
    position: absolute;
    left: 19px;
    top: 1781px;
    width: 375px;
    height: 580px;
    background: linear-gradient(180deg, var(--book-green) 0%, var(--book-green) 8%, var(--book-cream) 8%, var(--book-cream) 76%, var(--book-green) 76%, var(--book-green) 100%);
    box-shadow: 0 6px 18px rgba(0,0,0,0.15);
  }
  .book-reflection {
    position: absolute;
    left: 19px;
    top: 2365px;
    width: 375px;
    height: 220px;
    background: linear-gradient(180deg, rgba(63,122,58,0.3) 0%, rgba(255,255,255,0) 100%);
  }
  .expert-info {
    position: absolute;
    left: 82px;
    top: 2600px;
    width: 1100px;
    color: var(--ink);
  }
  .expert-name {
    font-size: 80px;
    font-weight: 400;
    line-height: 92px;
    margin-bottom: 70px;
  }
  .credentials {
    list-style: none;
    font-size: 40px;
    font-weight: 700;
    line-height: 54px;
    white-space: nowrap;
  }
</style>
</head>
<body>
  <main class="banner">
    <div class="heart-backdrop" role="img" aria-label="Soft pink background patterned with scattered pale hearts"></div>

    <p class="quote">"Successful,<br>rich, happy<br>owners<br>aren’t<br>smarter.<br>They just<br>play by a<br>different<br>set of<br>rules."</p>

    <div class="portrait" role="img" aria-label="Full-length photo of Ivo Venn standing in a black suit, arms crossed, legs crossed at the ankles"></div>
    <div class="portrait-reflection" role="img" aria-label="Faint floor reflection of the standing portrait"></div>

    <div class="book-cover" role="img" aria-label="Book cover: Quiet Habits Of Parlor Keepers And A Ladder Out Of Debt by Ivo Venn"></div>
    <div class="book-reflection" role="img" aria-label="Faint mirrored reflection of the book cover"></div>

    <section class="expert-info">
      <h1 class="expert-name">Ivo Venn</h1>
      <ul class="credentials">
        <li>#1 Business Expert In The Salon &amp; Spa<br>Industry</li>
        <li>Millionaire Salon Owner</li>
        <li>Best-Selling Author of Quiet Habits Of Parlor<br>Keepers And A Ladder Out Of Debt</li>
      </ul>
    </section>
  </main>
</body>
</html>
```